Small Accounting Practice needs something creative

We need a business card design for a new small accounting practice based in Perth, Australia. The name of the practice is 'Kelvarin Ledger Group Pty Ltd'. We providing Tax, Bookkeeping and Accounting services. Our target are individuals and small businesses. We want the design to be simply and creative. Also, we can the design can help us to gain people's trust.

Target Market(s)

Individuals and small businesses.

Industry/Entity Type

Accounting

Colors

Designer to choose colors to be used in the design.

```html
<!DOCTYPE html>
<html lang="en">
<head>
<meta charset="utf-8">
<title>Kelvarin Ledger Group Pty Ltd — Business Cards</title>
<link rel="stylesheet" href="https://fonts.googleapis.com/css2?family=PT+Sans:wght@400;700&family=PT+Sans+Narrow:wght@700&display=swap">
<style>
  :root {
    --backdrop: #e9e7e4;
    --card-dark: #4a4b4d;
    --card-light: #f7f9f9;
    --ink: #3a3b3d;
    --ink-white: #ffffff;
    --tagline-grey: #8a8b8d;
    --accent-blue: #5bc0ea;
    --shadow: rgba(0, 0, 0, 0.18);
  }
  html, body {
    margin: 0;
    padding: 0;
    width: 1200px;
    height: 1200px;
    overflow: hidden;
    background: var(--backdrop);
    font-family: "PT Sans", Arial, sans-serif;
  }
  .canvas {
    width: 1200px;
    height: 1200px;
    display: flex;
    flex-direction: column;
    align-items: center;
    justify-content: center;
    gap: 56px;
  }
  .card {
    width: 840px;
    height: 510px;
    position: relative;
    box-shadow: 0 10px 28px var(--shadow);
    overflow: hidden;
  }

  /* Front */
  .card--front {
    background: var(--card-dark);
    color: var(--ink-white);
  }
  .front__brand {
    position: absolute;
    left: 0;
    right: 0;
    top: 190px;
    display: flex;
    align-items: center;
    justify-content: center;
    gap: 18px;
  }
  .front__brand-square {
    width: 26px;
    height: 26px;
    background: var(--accent-blue);
  }
  .front__brand-name {
    font-size: 40px;
    font-weight: 400;
    letter-spacing: 0.2px;
    color: var(--ink-white);
  }
  .front__services {
    position: absolute;
    left: 0;
    right: 0;
    top: 300px;
    text-align: center;
    font-family: "PT Sans Narrow", "Arial Narrow", sans-serif;
    font-weight: 700;
    font-size: 34px;
    letter-spacing: 2px;
    color: var(--tagline-grey);
    text-transform: uppercase;
  }
  .front__services .divider {
    font-weight: 400;
    margin: 0 14px;
  }

  /* Back */
  .card--back {
    background: var(--card-light);
    color: var(--ink);
  }
  .back__band {
    position: absolute;
    left: 0;
    top: 0;
    bottom: 0;
    width: 62px;
    background: var(--card-dark);
  }
  .back__mark {
    position: absolute;
    left: 90px;
    top: 66px;
    width: 22px;
    height: 22px;
    background: var(--accent-blue);
  }
  .back__details {
    position: absolute;
    left: 128px;
    top: 56px;
  }
  .back__name {
    margin: 0;
    font-size: 30px;
    font-weight: 700;
    color: var(--ink);
    line-height: 1.2;
  }
  .back__title {
    margin: 6px 0 0;
    font-size: 27px;
    font-weight: 400;
    color: var(--ink);
  }
  .back__email {
    margin: 6px 0 0;
    font-size: 27px;
    color: var(--accent-blue);
  }
  .back__registration {
    position: absolute;
    right: 48px;
    bottom: 44px;
    font-size: 23px;
    color: var(--ink);
  }
</style>
</head>
<body>
  <main class="canvas">
    <section class="card card--front" aria-label="Business card front">
      <div class="front__brand">
        <span class="front__brand-square" aria-hidden="true"></span>
        <span class="front__brand-name">Kelvarin Ledger Group Pty Ltd</span>
      </div>
      <p class="front__services">Tax<span class="divider">|</span>Bookkeeping<span class="divider">|</span>Accounting</p>
    </section>

    <section class="card card--back" aria-label="Business card back">
      <div class="back__band"></div>
      <span class="back__mark" aria-hidden="true"></span>
      <div class="back__details">
        <p class="back__name">Tomas Reyne</p>
        <p class="back__title">Accountant &amp; Small Business Consultant</p>
        <p class="back__email">tomas@kelvarinledger.com.au</p>
      </div>
      <p class="back__registration">Registered ASIC Agent 48107</p>
    </section>
  </main>
</body>
</html>
```